Velora Shift Bundle Social Media Graphics

Focusing on the Velora Shift Bundle product, create 5-6 individual social media graphics (square size). For the color scheme of the graphics, they should all be complementary with the Velora Shift Bundle bottle colors.

Note: each graphic should have one of the pictures of the bottles (2-product bundle) on it and/or one of the images with a person on it (several pics attached)/only use stock photography that I provided.

Target Market(s)

women over 40 struggling with hormonal decline

Industry/Entity Type

health and weight loss

Requirements
Nice to have
• pictures attached

```html
<!DOCTYPE html>
<html lang="en">
<head>
<meta charset="utf-8">
<title>Velora Shift Bundle – Hormone Balance Post</title>
<link href="https://fonts.googleapis.com/css2?family=Inter:wght@400;500;700;800&display=swap" rel="stylesheet">
<style>
  :root {
    --frame: #9ccbbf;
    --frame-dark: #7fb3a6;
    --forest: #3d5c53;
    --forest-deep: #34504a;
    --sage: #6e948b;
    --pill: rgba(160, 196, 188, 0.45);
    --pill-badge: #6a8f86;
    --peach: #ead4c6;
    --sand: #d8c2b4;
    --white: #ffffff;
    --logo: #3f6057;
  }
  * { margin: 0; padding: 0; box-sizing: border-box; }
  html, body { width: 1200px; height: 1200px; overflow: hidden; }
  body {
    font-family: "Inter", Arial, sans-serif;
    background: linear-gradient(135deg, var(--frame) 0%, var(--frame-dark) 100%);
    position: relative;
  }
  .panel {
    position: absolute;
    left: 13px; top: 13px; width: 1174px; height: 1174px;
    border-radius: 14px;
    overflow: hidden;
    background: linear-gradient(180deg,
      var(--peach) 0%, var(--sand) 28%, #b8b3a6 40%,
      #849a90 50%, #5f7f75 58%, var(--forest) 72%, var(--forest-deep) 100%);
  }
  .hero-photo {
    position: absolute;
    left: 300px; top: 0; width: 760px; height: 760px;
    background: radial-gradient(ellipse at 55% 35%, rgba(190,150,130,0.55) 0%, rgba(150,130,120,0.35) 40%, rgba(120,140,130,0) 75%);
  }
  .logo {
    position: absolute; left: 42px; top: 30px;
    font-weight: 700; font-size: 57px; line-height: 1.0;
    color: var(--logo); letter-spacing: 1px;
  }
  .headline {
    position: absolute; left: 40px; top: 470px;
    color: var(--white);
  }
  .headline .lead { font-size: 38px; font-weight: 400; line-height: 48px; }
  .headline .big { font-size: 91px; font-weight: 800; line-height: 100px; letter-spacing: -1px; }
  .headline .tail { font-size: 38px; font-weight: 400; line-height: 46px; }

  .symptoms { position: absolute; left: 95px; top: 690px; list-style: none; }
  .symptom {
    position: relative;
    width: 392px; height: 78px; margin-bottom: 14px;
    border-radius: 39px;
    background: var(--pill);
    box-shadow: 4px 6px 6px rgba(20, 40, 35, 0.35);
    display: flex; align-items: center;
  }
  .symptom .num {
    width: 68px; height: 68px; margin-left: 5px;
    border-radius: 50%;
    background: var(--pill-badge);
    color: var(--white); font-weight: 700; font-size: 26px;
    display: flex; align-items: center; justify-content: center;
  }
  .symptom .label {
    margin-left: 30px;
    color: var(--white); font-weight: 700; font-size: 24px; line-height: 30px;
  }
  .product-ring {
    position: absolute; left: 596px; top: 670px;
    width: 438px; height: 438px; border-radius: 50%;
    background: var(--sage);
    display: flex; align-items: center; justify-content: center;
  }
  .product-photo {
    width: 412px; height: 412px; border-radius: 50%;
    background: radial-gradient(circle at 50% 45%, #f4f4f2 0%, #e6e7e4 60%, #d6d8d4 100%);
  }
  .timeline { position: absolute; left: 0; top: 0; }
</style>
</head>
<body>
  <div class="panel">
    <div class="hero-photo" role="img" aria-label="Smiling woman in a blue tank top flexing her arm and pointing at it"></div>

    <div class="logo">LOGO<br>HERE</div>

    <div class="headline">
      <p class="lead">Diet &amp; Exercise are a Waste of Time if</p>
      <p class="big">Your Hormones</p>
      <p class="tail">Are Out of Balance</p>
    </div>

    <ul class="symptoms">
      <li class="symptom"><span class="num">1</span><span class="label">Mood Swings</span></li>
      <li class="symptom"><span class="num">2</span><span class="label">Fatigue and Low<br>Motivation</span></li>
      <li class="symptom"><span class="num">3</span><span class="label">Weight gain;<br>Stubborn Belly Fat</span></li>
      <li class="symptom"><span class="num">4</span><span class="label">Hot flashes &amp;<br>Night Sweats</span></li>
      <li class="symptom"><span class="num">5</span><span class="label">Brain Fog &amp; Memory<br>Lapses</span></li>
    </ul>

    <div class="product-ring">
      <div class="product-photo" role="img" aria-label="Velora Shift Bundle: supplement bottle and Lumina Balance Cream pump on a light background"></div>
    </div>

    <svg class="timeline" width="1174" height="1174" viewBox="13 13 1174 1174">
      <path d="M790 661 A244 244 0 1 0 790 1143" fill="none" stroke="#ffffff" stroke-width="3"/>
      <g font-family="Inter, Arial, sans-serif" font-weight="700" font-size="21" fill="#2f4a43" text-anchor="middle">
        <circle cx="690" cy="700" r="20" fill="#ffffff" stroke="#2f4a43" stroke-width="3"/><text x="690" y="708">1</text>
        <circle cx="618" cy="778" r="20" fill="#ffffff" stroke="#2f4a43" stroke-width="3"/><text x="618" y="786">2</text>
        <circle cx="584" cy="902" r="20" fill="#ffffff" stroke="#2f4a43" stroke-width="3"/><text x="584" y="910">3</text>
        <circle cx="618" cy="1028" r="20" fill="#ffffff" stroke="#2f4a43" stroke-width="3"/><text x="618" y="1036">4</text>
        <circle cx="689" cy="1108" r="20" fill="#ffffff" stroke="#2f4a43" stroke-width="3"/><text x="689" y="1116">5</text>
      </g>
    </svg>
  </div>
</body>
</html>
```